Business cards for start-up accounting firm

I'm looking for a double sided business card ready for upload into Lumo print or similar print providers with no modification required by me.
I'm looking for something simple as i think cards that are too 'busy' actually detract from the message. I have some thoughts but more than happy to see what comes up. The logo i have came out of left field and i love it the moment i saw it!

My thoughts:

Side 1: Just the logo, perhaps on a dark grey or charcoal background to make the logo colours stand out?

Side 2: The call to action from me website 'Looking for a more relaxed, friendly and interactive relationship with your accountant?' with my contact information
Name: Gus Tarrow
Email: gus@ledgerowl.com.au
Website: www.ledgerowl.com.au
Phone: 1300 762 349

The call to action needs to be the first thing they see when they look at side 2. If it helps to know what we do and how we do it there is a draft website at www.ledgerowl.com.au

Like i said, happy to consider anything that comes up :)

Target Market(s)

i'm targeting small business owners who experience a lot of stress around finacial reporting and have had bad experiences with accountants in the past.

Industry/Entity Type

Accounting

Contact Information for Business Card

Contained in the Description

Font styles to use
Serif
Sans Serif
Other font styles liked:
• See logo files attached

Colors
474747

Requirements
Must have
• My logo, slogan and contact information

```html
<!DOCTYPE html>
<html lang="en">
<head>
<meta charset="utf-8">
<title>Ledger Owl – Business Card</title>
<link href="https://fonts.googleapis.com/css2?family=Roboto+Condensed:wght@400;500;700&family=Arimo:wght@700&family=Titillium+Web:wght@600&display=swap" rel="stylesheet">
<style>
  :root {
    --gold: #e3b017;
    --charcoal: #474747;
    --brand-yellow: #ffd400;
    --tagline-mauve: #b97ba9;
    --sage: #b2c598;
    --ink: #0d0d0d;
    --page: #ffffff;
  }
  * { box-sizing: border-box; margin: 0; padding: 0; }
  html, body { width: 1200px; height: 1200px; overflow: hidden; background: var(--page); }
  .sheet { position: relative; width: 1200px; height: 1200px; }

  .card {
    position: absolute;
    left: 176px;
    width: 869px;
    height: 508px;
    overflow: hidden;
    background: var(--gold);
  }
  .card--front { top: 52px; }
  .card--back { top: 618px; }

  .band {
    position: absolute;
    left: 0; right: 0; bottom: 0;
    background: linear-gradient(180deg, #3f3f3f 0%, var(--charcoal) 100%);
  }
  .card--front .band { height: 142px; }
  .card--back .band { height: 158px; }

  .brand-name {
    position: absolute;
    left: 40px; right: 40px;
    top: 190px;
    text-align: center;
    white-space: nowrap;
    font-family: "Roboto Condensed", sans-serif;
    font-weight: 700;
    font-size: 132px;
    line-height: 1;
    letter-spacing: 2px;
    color: var(--brand-yellow);
  }

  .tagline {
    position: absolute;
    left: 100px; right: 82px;
    top: 426px;
    display: flex;
    align-items: center;
    gap: 22px;
    font-family: "Titillium Web", sans-serif;
    font-weight: 600;
    font-size: 30px;
    letter-spacing: 5px;
    color: var(--tagline-mauve);
    white-space: nowrap;
  }
  .tagline::before, .tagline::after {
    content: "";
    flex: 1;
    height: 3px;
    background: var(--tagline-mauve);
  }

  .call-to-action {
    position: absolute;
    left: 37px;
    top: 60px;
    font-family: "Roboto Condensed", sans-serif;
    font-weight: 700;
    font-size: 34px;
    line-height: 40px;
    color: var(--ink);
    text-transform: uppercase;
    white-space: nowrap;
  }

  .contact-panel {
    position: absolute;
    left: 92px;
    top: 178px;
    width: 678px;
    height: 262px;
    border-radius: 52px;
    background: var(--sage);
    box-shadow: 10px 14px 22px rgba(0,0,0,0.45);
  }
  .contact-name {
    position: absolute;
    left: 68px;
    top: 20px;
    font-family: "Arimo", sans-serif;
    font-weight: 700;
    font-size: 35px;
    color: var(--ink);
    text-transform: uppercase;
  }
  .contact-list { list-style: none; position: absolute; left: 66px; top: 80px; }
  .contact-item {
    display: flex;
    align-items: center;
    height: 52px;
    font-family: "Roboto Condensed", sans-serif;
    font-weight: 500;
    font-size: 40px;
    color: var(--ink);
    white-space: nowrap;
  }
  .contact-icon { width: 40px; height: 40px; margin-right: 26px; flex: none; }
</style>
</head>
<body>
<main class="sheet">

  <section class="card card--front" aria-label="Card front">
    <div class="band"></div>
    <h1 class="brand-name">LEDGER OWL</h1>
    <p class="tagline">LESS STRESS, MORE SUCCESS</p>
  </section>

  <section class="card card--back" aria-label="Card back">
    <div class="band"></div>
    <p class="call-to-action">Looking for a more relaxed, friendly and<br>interactive relationship with your accountant ?</p>
    <div class="contact-panel">
      <h2 class="contact-name">Gus Tarrow</h2>
      <ul class="contact-list">
        <li class="contact-item">
          <svg class="contact-icon" viewBox="0 0 40 40" aria-hidden="true">
            <path d="M0 14 L20 2 L40 14 V38 H0 Z" fill="var(--ink)"/>
            <text x="20" y="30" text-anchor="middle" font-family="Arial, sans-serif" font-size="13" fill="var(--sage)">@</text>
          </svg>
          gus@ledgerowl.com.au
        </li>
        <li class="contact-item">
          <svg class="contact-icon" viewBox="0 0 40 40" aria-hidden="true">
            <path d="M10 2 C5 4 3 10 5 18 C8 28 15 36 24 39 C28 40 31 38 33 35 L27 28 C25 29 23 30 21 28 C17 24 14 19 14 14 C14 12 15 11 17 10 L14 2 Z" fill="var(--ink)"/>
          </svg>
          1300 762 349
        </li>
        <li class="contact-item">
          <svg class="contact-icon" viewBox="0 0 40 40" aria-hidden="true">
            <circle cx="20" cy="20" r="19" fill="var(--ink)"/>
            <g stroke="var(--sage)" stroke-width="1.6" fill="none">
              <ellipse cx="20" cy="20" rx="8" ry="19"/>
              <line x1="20" y1="1" x2="20" y2="39"/>
              <line x1="1" y1="20" x2="39" y2="20"/>
              <path d="M4 11 H36 M4 29 H36"/>
            </g>
          </svg>
          www.ledgerowl.com.au
        </li>
      </ul>
    </div>
  </section>

</main>
</body>
</html>
```